Quellmar Aus Business card revamp

We are looking to revamp our business card design. We are hoping to change our colours to dark navey blue, gray, white and black but are open to keeping the same if a good design is submited. We are after somthing a bit differnt not just boring business card. I have attached a copy of our current card. We Want to keep the same logo design which i have attached a few to hopfully help you in this process. We are after a design that can be personalized to separate 4 people

Industry/Entity Type

Business

Colors
0455a3
ffffff
000000
cbcbcb

Requirements
Must have
• Quellmar Logo, address 3/41 Wattlebend Street, Kelvanby 4517, phone number, Name and position

```html
<!DOCTYPE html>
<html lang="en">
<head>
<meta charset="utf-8">
<title>Quellmar Aus – Business Card</title>
<link href="https://fonts.googleapis.com/css2?family=Open+Sans:wght@400;600;800&display=swap" rel="stylesheet">
<style>
  :root {
    --backdrop: #3a322e;
    --card: #0d0d0d;
    --brand-blue: #2f86d1;
    --brand-orange: #f27a1a;
    --text-white: #f2f2f2;
    --silver: #cbcbcb;
    --divider: #3a3a3a;
  }
  * { margin: 0; padding: 0; box-sizing: border-box; }
  html, body {
    width: 1200px; height: 900px; overflow: hidden;
    background: var(--backdrop);
    font-family: "Open Sans", sans-serif;
  }
  .stage {
    position: relative; width: 1200px; height: 900px;
    display: flex; align-items: center; justify-content: center; gap: 50px;
  }
  .card {
    position: relative; width: 530px; height: 303px;
    background: var(--card);
    box-shadow: 0 18px 40px rgba(0,0,0,.55);
  }
  .brand { display: flex; align-items: center; gap: 12px; }
  .brand-mark {
    width: 44px; height: 44px; border-radius: 50%;
    background: var(--brand-orange);
  }
  .brand-name {
    font-weight: 800; font-size: 46px; line-height: 1; letter-spacing: -1px;
    color: var(--brand-blue);
  }
  .brand-tagline {
    font-weight: 800; font-size: 19px; color: var(--brand-orange);
    margin: 4px 0 0 56px;
  }
  /* front */
  .card-front .brand-block { position: absolute; left: 34px; top: 34px; }
  .contact {
    position: absolute; left: 196px; top: 152px;
    color: var(--text-white); font-size: 13px; white-space: nowrap;
  }
  .person-name { font-weight: 600; font-size: 17px; line-height: 22px; color: var(--brand-blue); }
  .person-name .surname { color: var(--brand-orange); }
  .person-role { margin-bottom: 16px; line-height: 19px; }
  .contact-line { display: flex; align-items: center; gap: 8px; line-height: 22px; }
  .contact-line svg { width: 11px; height: 11px; fill: var(--brand-orange); flex: none; }
  .divider {
    position: absolute; left: 392px; top: 152px;
    width: 1px; height: 108px; background: var(--divider);
  }
  .company-info {
    position: absolute; left: 406px; top: 152px; width: 108px;
    color: var(--text-white); font-size: 13px; line-height: 21px; white-space: nowrap;
  }
  .company-info .label { color: var(--brand-orange); }
  /* back */
  .card-back { display: flex; flex-direction: column; align-items: center; justify-content: center; }
  .card-back .brand-name { color: var(--silver); }
  .card-back .brand-mark { background: var(--silver); }
  .card-back .brand-tagline { color: var(--silver); }
  .social { display: flex; gap: 10px; margin-top: 22px; }
  .social-dot { width: 22px; height: 22px; border-radius: 50%; background: var(--brand-orange); }
</style>
</head>
<body>
<main class="stage">
  <section class="card card-front" aria-label="Card front">
    <div class="brand-block">
      <div class="brand">
        <span class="brand-mark"></span>
        <span class="brand-name">Quellmar</span>
      </div>
      <div class="brand-tagline">Passive Fire Protection</div>
    </div>

    <div class="contact">
      <div class="person-name">Dana <span class="surname">Merrow</span></div>
      <div class="person-role">Project Coordinator</div>
      <div class="contact-line">
        <svg viewBox="0 0 24 24"><path d="M6.6 10.8a15 15 0 0 0 6.6 6.6l2.2-2.2c.3-.3.7-.4 1-.2 1.1.4 2.3.6 3.6.6.6 0 1 .4 1 1V20c0 .6-.4 1-1 1A17 17 0 0 1 3 4c0-.6.4-1 1-1h3.5c.6 0 1 .4 1 1 0 1.3.2 2.5.6 3.6.1.3 0 .7-.2 1z"/></svg>
        07 5550 2184
      </div>
      <div class="contact-line">
        <svg viewBox="0 0 24 24"><path d="M2 5h20v14H2z M2 5l10 8 10-8"/></svg>
        admin@quellmar.com.au
      </div>
      <div class="contact-line">
        <svg viewBox="0 0 24 24"><circle cx="12" cy="12" r="10"/></svg>
        www.quellmar.co.au
      </div>
    </div>

    <div class="divider"></div>

    <div class="company-info">
      <div><span class="label">ABN:</span> 11224466</div>
      <div>3/41 Wattlebend</div>
      <div>Street, Kelvanby</div>
      <div>4517</div>
    </div>
  </section>

  <section class="card card-back" aria-label="Card back">
    <div>
      <div class="brand">
        <span class="brand-mark"></span>
        <span class="brand-name">Quellmar</span>
      </div>
      <div class="brand-tagline">Passive Fire Protection</div>
    </div>
    <div class="social">
      <span class="social-dot"></span>
      <span class="social-dot"></span>
    </div>
  </section>
</main>
</body>
</html>
```